Bluewater Motor Finance Home Page

We need a desktop version mock up (we will base our mobile version off of this) of a website homepage for our auto loan business, Bluewater Motor Finance. This does not need to be a functioning site, just a home page mock up. We are based in the metro St. Louis, MO area. We offer "guaranteed" auto loans for all credit types. We specialize in financing for bad/no credit customers. We are able to help rebuild these type of customers' credit, all while putting them in a great late model vehicle they'll love. Our online credit app takes less than 60 seconds, doesn't require a SS# and gives a free credit score if they fill it out within 3 minutes. We are looking for an outside perspective to help us in this design process. We are not completely sure what we want, but we do want it to be professional and secure looking, all while being unique and aesthetically pleasing. We want the customer to be able to put in their zip code to be directed to the right location that can get them pre approved. I attached a wireframe with some stuff we'd like to include, but in no way does it have to be in the same layout or the same ideas. We want everyone to "go crazy" with their creative side on this. Our current site is awful, here is a link to get a better idea: www.bluewatermotorfinance-example.com. Attached is our logo too, base colors off of it. Watch our video that is also attached for a better idea.

Target Market(s)

Residents of the St. Louis Missouri Metro Area that need an auto loan. 24-55 Male and Female - Lots of "urban market" customers.

Industry/Entity Type

Loan

Number of Pages Required

1 page

Colors
9bcb3b

Requirements
Must have
• An area where the customer can enter their zip code - Be creative!
Nice to have
• See wireframe attachment for ideas - Be creative!

```html
<!DOCTYPE html>
<html lang="en">
<head>
<meta charset="utf-8">
<title>Bluewater Motor Finance</title>
<link href="https://fonts.googleapis.com/css2?family=Montserrat:wght@700&family=Raleway:wght@400;500;600;700&display=swap" rel="stylesheet">
<style>
:root{
  --green:#2ea84a;
  --lime:#8dc63f;
  --lime-dark:#6ea62b;
  --ink:#222;
  --text:#444;
  --muted:#666;
  --rule:#cfcfcf;
  --dark:#2a2a2a;
  --darker:#1c1c1c;
  --white:#fff;
  --badge:#f2e500;
}
*{box-sizing:border-box;margin:0;padding:0}
html,body{width:709px;height:1200px;overflow:hidden}
body{font-family:"Raleway",sans-serif;color:var(--text);background:var(--white);position:relative}
.abs{position:absolute}
/* header */
.site-header{position:absolute;left:0;top:0;width:709px;height:61px;background:#fbf8f8;border-top:3px solid #333;border-bottom:1px solid var(--lime)}
.brand{position:absolute;left:58px;top:14px;display:flex;align-items:center;gap:6px;font-weight:700;font-size:15px;color:var(--green)}
.brand-mark{width:14px;height:14px;background:var(--green)}
.phone-tab{position:absolute;left:536px;top:-3px;width:110px;height:20px;background:var(--darker);border-radius:0 0 14px 14px;color:var(--white);font-weight:700;font-size:10px;display:flex;align-items:center;justify-content:center;gap:5px}
.main-nav{position:absolute;left:300px;top:34px;display:flex;gap:0;font-size:7.5px;font-weight:500;color:var(--ink)}
.main-nav a{color:inherit;text-decoration:none;position:absolute;white-space:nowrap}
/* hero */
.hero{position:absolute;left:0;top:61px;width:709px;height:277px;background:linear-gradient(100deg,#c7a2a6 0%,#d9c0c2 35%,#e6dedd 60%,#cfc8c6 100%)}
.hero h1{position:absolute;left:59px;top:91px;font-family:"Montserrat",sans-serif;font-size:14.5px;color:var(--white);letter-spacing:.2px}
.hero .lead{position:absolute;left:60px;top:113px;font-size:10px;color:var(--white)}
.perks{position:absolute;left:60px;top:138px;list-style:none;display:grid;grid-template-columns:178px 110px;row-gap:4px;font-size:7.8px;color:#fff}
.perks li::before{content:"";display:inline-block;width:5px;height:5px;background:#333;transform:rotate(45deg);margin-right:7px}
.zip{position:absolute;left:59px;top:181px;width:130px;height:24px;border:1px solid #fff;color:#fff;font-size:7px;padding:7px 8px;background:rgba(255,255,255,.06)}
.btn{background:linear-gradient(#9ccf4a,#7cb533);color:#fff;font-size:8px;display:flex;align-items:center;justify-content:center;border-radius:1px}
.zip-btn{position:absolute;left:217px;top:181px;width:74px;height:24px}
/* section heads */
.sec-title{position:absolute;left:0;width:709px;text-align:center;font-size:18.5px;font-weight:400}
.sec-title span{color:var(--green)}
.divider{position:absolute;left:144px;width:420px;height:1px;background:var(--rule)}
.divider i{position:absolute;left:205px;top:-4px;width:9px;height:9px;background:var(--green)}
.copy{position:absolute;left:62px;width:585px;text-align:center;font-size:7.6px;line-height:15.5px}
/* locations */
.locations{position:absolute;left:0;top:519px;width:709px;height:213px;background:linear-gradient(110deg,#4a4b50 0%,#5c5856 50%,#6f625c 70%,#4e4d4f 100%);color:#fff}
.loc{position:absolute;top:129px;display:flex;align-items:center;gap:14px;font-size:11px;line-height:13px}
.loc-disc{width:46px;height:46px;border-radius:50%;background:#fff;position:relative;display:flex;align-items:center;justify-content:center}
.loc-disc b{width:13px;height:13px;background:var(--green)}
.loc-num{position:absolute;left:-7px;top:-3px;width:17px;height:17px;border-radius:50%;background:var(--badge);color:#333;font-size:6.5px;display:flex;align-items:center;justify-content:center;font-weight:600}
/* cta */
.cta{position:absolute;left:0;top:732px;width:709px;height:53px;background:var(--green);color:#fff}
.cta p{position:absolute;left:59px;top:13px;font-size:11px;line-height:16px}
.cta-btn{position:absolute;left:505px;top:14px;width:105px;height:25px;background:var(--darker);color:#fff;font-size:8px;display:flex;align-items:center;justify-content:center}
/* testimonials & video */
.col-title{position:absolute;top:811px;font-size:18px;color:var(--ink)}
.col-title span{color:var(--green)}
.col-rule{position:absolute;top:838px;height:1px;background:#ddd}
.col-rule::before{content:"";position:absolute;left:0;top:-1px;width:54px;height:2px;background:#999}
.reviews{position:absolute;left:58px;top:848px;width:285px;height:122px;background:#e8e8e8}
.review{position:absolute;left:8px;display:flex;gap:10px}
.avatar{width:37px;height:37px;border-radius:50%;border:2px solid #fff;background:linear-gradient(#a78b74,#6e5848);flex:none}
.review h4{font-size:7.5px;color:var(--ink);margin:3px 0 2px}
.review p{font-size:6.8px;line-height:10.5px;width:220px;color:#555}
.pager{position:absolute;left:316px;top:971px;width:20px;height:9px;background:#ddd;font-size:7px;color:#777;text-align:center;line-height:9px}
.video{position:absolute;left:396px;top:846px;width:255px;height:135px;border:2px solid #ddd;background:#fff}
.video-still{position:absolute;left:1px;top:1px;width:249px;height:110px;background:linear-gradient(100deg,#8c6e5c,#c9a595 45%,#d9d1cc 75%,#b9b2ae)}
.play{position:absolute;left:109px;top:39px;width:26px;height:26px;border-radius:50%;background:#fff}
.controls{position:absolute;left:1px;top:111px;width:249px;height:20px;background:#1a1a1a;color:#fff;font-size:6.5px}
.bar{position:absolute;left:50px;top:8px;width:143px;height:5px;background:#444;border-radius:3px}
.bar i{position:absolute;left:0;top:0;width:38px;height:5px;background:#d11;border-radius:3px}
.bar b{position:absolute;left:35px;top:-1px;width:7px;height:7px;border-radius:50%;background:#ccc}
/* footer */
.site-footer{position:absolute;left:0;top:1006px;width:709px;height:168px;background:var(--dark);color:#ddd}
.f-head{position:absolute;top:25px;font-size:8.5px;font-weight:700;color:#fff}
.f-head span{color:var(--lime)}
.f-head::after{content:"";position:absolute;left:0;top:15px;height:1px;background:#444;width:var(--w)}
.links{position:absolute;left:59px;top:53px;list-style:none;font-size:7.3px;line-height:18.3px}
.links li::before{content:"• ";}
.links li:first-child{color:var(--lime)}
.contact{position:absolute;left:179px;top:52px;font-size:7.2px;line-height:10.5px;width:140px}
.contact .row{display:flex;gap:7px;align-items:center;margin-top:10px}
.map{position:absolute;left:347px;top:48px;width:167px;height:102px;border:2px solid #fff;background:linear-gradient(135deg,#e6e2da,#d5d6cc)}
.social{position:absolute;left:565px;display:flex;gap:10px;align-items:center;font-size:8px;color:#fff;line-height:8px}
.social i{width:20px;height:20px;border-radius:50%;flex:none}
.social small{display:block;font-size:5.5px}
.copyright{position:absolute;left:0;top:1174px;width:709px;height:26px;background:#161616;color:#ccc;font-size:6.8px;text-align:center;line-height:26px}
</style>
</head>
<body>

<header class="site-header">
  <div class="brand"><span class="brand-mark"></span>Bluewater Motor Finance</div>
  <div class="phone-tab">
    <svg width="9" height="9" viewBox="0 0 24 24"><path fill="#8dc63f" d="M6.6 10.8a15 15 0 006.6 6.6l2.2-2.2c.3-.3.7-.4 1-.2 1.1.4 2.3.6 3.6.6.6 0 1 .4 1 1V20c0 .6-.4 1-1 1A17 17 0 013 4c0-.6.4-1 1-1h3.5c.6 0 1 .4 1 1 0 1.3.2 2.5.6 3.6.1.3 0 .7-.2 1z"/></svg>
    (800) 555-0142
  </div>
  <nav class="main-nav">
    <a style="left:3px;top:-3px"><svg width="11" height="10" viewBox="0 0 24 22"><path fill="#2ea84a" d="M12 1 1 11h3v10h6v-6h4v6h6V11h3z"/></svg></a>
    <a style="left:41px;top:-4px">LOCATIONS</a>
    <a style="left:114px;top:0">FINANCE CENTER</a>
    <a style="left:210px;top:0">ABOUT</a>
    <a style="left:267px;top:0">FAQ</a>
    <a style="left:312px;top:0">CONTACT</a>
  </nav>
</header>

<section class="hero" role="img" aria-label="Hand holding a car key fob in front of a blurred red car">
  <svg class="abs" style="left:17px;top:117px" width="22" height="42"><path d="M21 1 1 21l20 20" fill="none" stroke="#888" stroke-width="1"/></svg>
  <svg class="abs" style="left:668px;top:117px" width="22" height="42"><path d="M1 1l20 20L1 41" fill="none" stroke="#999" stroke-width="1"/></svg>
  <h1>OVER 30,000 AUTO LOANS SINCE 2000</h1>
  <p class="lead">Pre-Approval in Under 60 Seconds!</p>
  <ul class="perks">
    <li>No Social Security Number Required</li><li>No Application Fees</li>
    <li>Instant Approval</li><li>All Credit Accepted</li>
  </ul>
  <div class="zip">Enter Zip Code</div>
  <div class="btn zip-btn">Get Approved</div>
</section>

<section class="welcome">
  <h2 class="sec-title" style="top:360px;color:var(--ink)">Welcome To <span>Bluewater Motor Finance</span></h2>
  <div class="divider" style="top:392px"><i></i></div>
  <p class="copy" style="top:403px">Lorem ipsum dolor sit amet, consectetuer adipiscing elit, sed diam nonummy nibh euismod tincidunt ut laoreet dolore magna aliquam erat volutpat. Ut wisi enim ad minim veniam, quis nostrud exerci tation ullamcorper suscipit lobortis nisl ut aliquip ex ea commodo consequat. Duis autem vel eum iriure dolor in hendrerit in vulputate velit esse molestie consequat, vel illum dolore eu feugiat nulla facilim veniam, quis nostrud exerci tation ullamcorper suscipit lobortis nisl ut aliquip ex ea commodo consequat. Duis autem vel eusan et iim qui blandit p</p>
  <div class="btn abs" style="left:321px;top:474px;width:67px;height:23px">Read More</div>
</section>

<section class="locations" role="img" aria-label="Smiling woman behind the wheel of a car, darkened background">
  <h2 class="sec-title" style="top:21px;color:#fff">Choose Your Location <span>&amp; Get Started</span></h2>
  <div class="divider" style="top:53px;background:#888"><i></i></div>
  <p class="copy" style="top:71px;left:75px;width:560px;color:#eee">Diam nonummy nibh euismod tincidunt ut laoreet dolore magna aliquam erat volutpat. Ut wisi enim ad minim veniam, quis nostrud exerci tation ullamcorper suscipit loboDuis autem vel eum iriure dolor in hendrerit in vulputate velit esse molestie</p>
  <div class="loc" style="left:115px"><div class="loc-disc"><span class="loc-num">01</span><b></b></div>St. Louis<br>Credit From</div>
  <div class="loc" style="left:298px"><div class="loc-disc"><span class="loc-num">02</span><b></b></div>St. Charles<br>Credit From</div>
  <div class="loc" style="left:482px"><div class="loc-disc"><span class="loc-num">03</span><b></b></div>Illinois<br>Credit From</div>
</section>

<section class="cta">
  <p>Ut wisi enim ad minim veniam, quis nostrud exerci tation ullamc consequat.<br>Duis autem vel eum iriure dolor in hendrerit in......</p>
  <div class="cta-btn">Calculate Payment</div>
</section>

<section class="testimonials">
  <h2 class="col-title" style="left:58px">Client <span>Testimonials</span></h2>
  <div class="col-rule" style="left:58px;width:285px"></div>
  <div class="reviews">
    <div class="review" style="top:13px"><div class="avatar" role="img" aria-label="Client portrait"></div><div><h4>Mr. Marcus Hale</h4><p>Lorem ipsum dolor sit amet, consectetuer adipiscing elit, sed diam nonummy nibh euismod tincidunt.</p></div></div>
    <div class="abs" style="left:8px;top:62px;width:265px;height:1px;background:#ccc"></div>
    <div class="review" style="top:73px"><div class="avatar" role="img" aria-label="Client portrait" style="background:linear-gradient(#e4c99a,#c99c70)"></div><div><h4>Miss. Tara Hale</h4><p>Lorem ipsum dolor sit amet, consectetuer adipiscing elit, sed diam nonummy nibh euismod tincidunt.</p></div></div>
  </div>
  <div class="pager">‹ ›</div>
  <div class="abs" style="left:367px;top:800px;width:1px;height:180px;background:#eee"></div>
</section>

<section class="video-block">
  <h2 class="col-title" style="left:396px">Watch <span>Our Video</span></h2>
  <div class="col-rule" style="left:396px;width:255px"></div>
  <div class="video">
    <div class="video-still" role="img" aria-label="Couple reviewing loan paperwork at home"></div>
    <div class="play"><svg width="26" height="26"><path d="M10 7v12l10-6z" fill="#111"/></svg></div>
    <div class="controls">
      <svg class="abs" style="left:8px;top:6px" width="8" height="8"><path d="M1 0v8l7-4z" fill="#fff"/></svg>
      <span class="abs" style="left:26px;top:6px">04:59</span>
      <div class="bar"><i></i><b></b></div>
      <span class="abs" style="left:199px;top:6px">10:35</span>
      <svg class="abs" style="left:222px;top:5px" width="10" height="10"><path d="M1 3h2l3-3v10L3 7H1z" fill="#fff"/></svg>
      <svg class="abs" style="left:237px;top:5px" width="10" height="10"><path d="M1 1l8 8M1 1h3M1 1v3M9 9H6M9 9V6" stroke="#fff" fill="none"/></svg>
    </div>
  </div>
</section>

<footer class="site-footer">
  <h3 class="f-head" style="left:59px;--w:68px">QUICK <span>LINKS</span></h3>
  <ul class="links"><li>Home</li><li>Locations</li><li>Finance Center</li><li>About</li><li>Faq</li><li>Contact Us</li></ul>

  <h3 class="f-head" style="left:179px;--w:118px">CONTACT <span>INFORMATION</span></h3>
  <div class="contact">
    <strong style="color:#fff;font-size:7.2px">BLUEWATER MOTOR FINANCE</strong><br>Lorem ipsum dolor sit amet,<br>consectet nibh e tincidunt 0123
    <div class="row" style="margin-top:12px"><svg width="8" height="8" viewBox="0 0 24 24"><path fill="#ddd" d="M6.6 10.8a15 15 0 006.6 6.6l2.2-2.2c.3-.3.7-.4 1-.2 1.1.4 2.3.6 3.6.6.6 0 1 .4 1 1V20c0 .6-.4 1-1 1A17 17 0 013 4c0-.6.4-1 1-1h3.5c.6 0 1 .4 1 1 0 1.3.2 2.5.6 3.6.1.3 0 .7-.2 1z"/></svg>(800) 555-0142</div>
    <div class="row"><svg width="8" height="9"><rect x="1.5" y=".5" width="5" height="8" rx="1" fill="none" stroke="#ddd"/></svg>555.014.2211</div>
    <div class="row"><svg width="8" height="6"><rect x=".5" y=".5" width="7" height="5" fill="none" stroke="#ddd"/><path d="M.5.5l3.5 3 3.5-3" fill="none" stroke="#ddd"/></svg>info@bluewatermotorfinance-example.com</div>
  </div>

  <h3 class="f-head" style="left:347px;--w:167px">LOCATION <span>MAP</span></h3>
  <div class="map" role="img" aria-label="Street map showing the office location"></div>

  <h3 class="f-head" style="left:565px;--w:85px">FOLLOW <span>US</span></h3>
  <div class="social" style="top:54px"><i style="background:#3b5998"></i><div>FRIENDSPACE<small>BECOME A FAN</small></div></div>
  <div class="social" style="top:91px"><i style="background:#0e76a8"></i><div>WORKLINE<small>JOIN US ON</small></div></div>
  <div class="social" style="top:127px"><i style="background:#2aa9e0"></i><div>CHIRPER<small>JOIN US ON</small></div></div>
</footer>
<div class="copyright">© 2016 Bluewatermotorfinance-example. All Rights Reserved.</div>

</body>
</html>
```